Natural Medicine & Health/Fitness Coaching studio requires web page

Require a innovative web page for a studio that coaches clients to better health, nutrition and fitness. The studio compromises of Clinical Nutritionists, Naturopaths, Rehab Trainers, Personal Trainers and Sport Coaches. Would like to see earthy but bold designs emphasizing nutritional health and athletic performance.
Updates

Design only launched today.

Target Market(s)

All genders from 20's to 60's, as well as families

Industry/Entity Type

Nutritionist

Coding

Coded - Design and coding required

Number of Pages Required

3 page

Colors
abd037
3277b5
fbee3d
fece3e
33b8a4
f04a50

Requirements
Must have
• Online booking system, ability to message
• Home page
• Coaching/Fitness page
• Nutritional Medicine page
• Must be suitable for both Fitness and Nutrition

```html
<!DOCTYPE html>
<html lang="en">
<head>
<meta charset="utf-8">
<title>Verdant Core — Nutritional Therapy</title>
<link href="https://fonts.googleapis.com/css2?family=Montserrat:wght@400;500;600;700;800&family=Open+Sans:wght@400;600&family=Lato:wght@700&display=swap" rel="stylesheet">
<style>
:root{
  --green:#0ea24b;
  --green-deep:#0b9446;
  --lime:#8dc63f;
  --blue:#1672b3;
  --sky:#2aa8e0;
  --navy:#1d5a8a;
  --footer:#1c4a78;
  --ink:#444;
  --muted:#666;
  --white:#fff;
  --dark:#232323;
}
*{margin:0;padding:0;box-sizing:border-box}
html,body{width:1200px;height:3273px;overflow:hidden}
body{position:relative;background:var(--white);font-family:'Open Sans',sans-serif;color:var(--ink)}
.abs{position:absolute}
.heading{font-family:'Montserrat',sans-serif;font-weight:700;color:var(--white);letter-spacing:.5px}

/* header / hero */
.hero{left:0;top:0;width:1200px;height:578px;background:linear-gradient(90deg,#fdfdfd 0%,#f4f6f7 45%,#e7ecef 100%)}
.logo{left:92px;top:30px;display:flex;align-items:center;gap:10px;font-family:'Montserrat',sans-serif;font-weight:600;font-size:40px;color:var(--green)}
.logo-dot{width:14px;height:14px;border-radius:50%;background:var(--lime)}
.nav{left:505px;top:56px;display:flex;gap:28px;font-family:'Montserrat',sans-serif;font-size:15px;color:#333}
.nav span{padding:6px 0}
.nav .active{border:2px solid var(--green);padding:4px 8px;color:var(--navy);font-weight:700}
.hero-photo{left:430px;top:120px;width:720px;height:458px;background:radial-gradient(ellipse at 55% 45%,#e8d9cf 0%,#dfe5ea 40%,rgba(231,236,239,0) 75%)}
.welcome{left:92px;top:210px;font-family:'Montserrat',sans-serif;font-weight:500;font-size:30px;color:#555}
.brand-title{left:92px;top:258px;font-family:'Montserrat',sans-serif;font-weight:700;font-size:46px;color:var(--navy);letter-spacing:1px}
.hero-text{left:92px;top:318px;width:330px;font-size:15px;line-height:28px;color:var(--muted)}
.btn-outline-green{left:92px;top:400px;width:112px;height:34px;border:2px solid var(--green);color:var(--green);font-family:'Montserrat',sans-serif;font-weight:600;font-size:14px;display:flex;align-items:center;justify-content:center}

/* about */
.about-bg{left:0;top:578px;width:1200px;height:560px;background:linear-gradient(135deg,#2a2a2a 0%,#1e1e1e 55%,#2f2f2f 100%)}
.video{left:92px;top:711px;width:467px;height:314px;background:linear-gradient(135deg,#7d8a3c 0%,#98a54a 45%,#6f7d37 100%)}
.play{left:280px;top:822px}
.about-title{left:600px;top:706px;font-size:29px}
.about-title em{font-style:normal;color:var(--green)}
.about-text{left:600px;top:792px;width:540px;font-size:14px;line-height:45px;color:var(--white)}
.btn-outline-white{border:2px solid var(--white);color:var(--white);font-family:'Montserrat',sans-serif;font-weight:600;font-size:14px;display:flex;align-items:center;justify-content:center}
.about-btn{left:600px;top:980px;width:140px;height:36px}

/* coaching */
.coach-bg{left:0;top:1113px;width:1200px;height:567px;background:linear-gradient(180deg,var(--green) 0%,#0a8f72 50%,var(--blue) 100%)}
.coach-title{left:0;top:1206px;width:1200px;text-align:center;font-size:27px}
.coach-text{left:92px;top:1328px;width:520px;font-size:14px;line-height:37.5px;color:var(--white)}
.coach-btn{left:92px;top:1503px;width:142px;height:36px}
.coach-photo{left:665px;top:1255px;width:425px;height:425px;background:linear-gradient(180deg,rgba(255,255,255,0) 0%,rgba(40,70,120,.35) 40%,rgba(20,30,50,.55) 100%);border-radius:200px 200px 0 0}

/* services */
.services-bg{left:0;top:1680px;width:1200px;height:470px;background:linear-gradient(135deg,#2b2a26 0%,#1d1d1b 50%,#2a2a28 100%)}
.services-title{left:0;top:1730px;width:1200px;text-align:center;font-size:28px}
.service-img{width:184px;height:184px;border-radius:50%;border:6px solid var(--green);box-shadow:0 0 0 4px var(--blue)}
.s1{left:155px;top:1795px;background:radial-gradient(circle,#b34545 0%,#6f9a44 70%)}
.s2{left:508px;top:1795px;background:radial-gradient(circle,#a07a62 0%,#3e3a3a 75%)}
.s3{left:859px;top:1795px;background:radial-gradient(circle,#e2cf9e 0%,#5aa8b0 75%)}
.service-label{width:300px;text-align:center;font-family:'Lato',sans-serif;font-weight:700;font-size:20px;line-height:32px;color:var(--white)}

/* testimonial */
.testi-bg{left:0;top:2138px;width:1200px;height:470px;background:linear-gradient(135deg,var(--blue) 0%,#0e8a86 50%,var(--green) 100%)}
.avatar{left:540px;top:2173px}
.t-name{left:0;top:2318px;width:1200px;text-align:center;font-family:'Montserrat',sans-serif;font-weight:700;font-size:18px;color:var(--white)}
.t-place{left:0;top:2346px;width:1200px;text-align:center;font-size:14px;color:var(--white)}
.t-quote{left:220px;top:2398px;width:760px;text-align:center;font-size:21px;line-height:34px;color:var(--white)}
.dots{left:533px;top:2533px;display:flex;gap:22px;align-items:center}
.dots span{width:6px;height:6px;border-radius:50%;background:rgba(255,255,255,.55)}
.dots .on{background:var(--white);width:7px;height:7px}
.dots-line{left:538px;top:2536px;width:124px;height:1px;background:rgba(255,255,255,.45)}

/* booking */
.book-bg{left:0;top:2607px;width:1200px;height:572px;background:linear-gradient(135deg,#2f2a24 0%,#1f1d1b 55%,#2e2b28 100%)}
.book-title{left:0;top:2668px;width:1200px;text-align:center;font-size:28px}
.form{left:240px;top:2771px;width:369px;height:325px;background:linear-gradient(180deg,var(--green) 0%,#0a8c7a 55%,var(--blue) 100%);padding:28px 32px}
.field{position:relative;height:44px;border-bottom:1.5px solid rgba(255,255,255,.85);margin-bottom:0;font-family:'Montserrat',sans-serif;font-size:12px;font-weight:500;color:var(--white);padding-top:10px}
.field svg{position:absolute;right:6px;top:14px}
.field.msg{height:78px}
.submit{margin-top:22px;width:146px;height:40px;background:var(--white);color:var(--navy);font-family:'Montserrat',sans-serif;font-weight:600;font-size:16px;display:flex;align-items:center;justify-content:center}
.contact{left:692px;top:2768px;width:340px;color:var(--white)}
.contact h3{font-family:'Montserrat',sans-serif;font-weight:700;font-size:26px;margin-bottom:24px}
.c-label{font-family:'Montserrat',sans-serif;font-weight:600;font-size:12px;letter-spacing:.3px}
.c-value{font-family:'Montserrat',sans-serif;font-size:15px;margin-bottom:26px}
.social{display:flex;gap:30px;margin-top:14px}
.social span{width:16px;height:16px;border-radius:50%;background:var(--white)}

/* footer */
.footer{left:0;top:3179px;width:1200px;height:94px;background:var(--footer);display:flex;align-items:center;justify-content:center;font-size:11px;color:var(--white)}
</style>
</head>
<body>

<!-- Hero -->
<div class="abs hero"></div>
<div class="abs hero-photo" role="img" aria-label="Smiling nutritionist in a white coat at a laptop with floating healthy meal images"></div>
<div class="abs logo"><span class="logo-dot"></span>Verdant Core</div>
<nav class="abs nav">
  <span class="active">HOME</span><span>ABOUT US</span><span>COACHING</span><span>FITNESS</span><span>NUTRITION</span><span>CONTACT US</span>
</nav>
<div class="abs welcome">WELCOME TO</div>
<div class="abs brand-title">VERDANT CORE</div>
<p class="abs hero-text">Lorem ipsum dolor sit amet, consectetur adipiscing elit, sed do eiusmod tempor</p>
<div class="abs btn-outline-green">Read more</div>

<!-- About -->
<div class="abs about-bg" role="img" aria-label="Dark background photo of healthy food and fitness gear"></div>
<svg class="abs" style="left:0;top:578px" width="1200" height="90" viewBox="0 0 1200 90">
  <polygon points="0,0 1200,0 0,70" fill="#ffffff"/>
  <polygon points="0,0 420,0 0,36" fill="var(--green)" opacity=".9"/>
  <polygon points="0,60 260,22 0,90" fill="var(--green)" opacity=".55"/>
</svg>
<div class="abs video" role="img" aria-label="Video still of fruit, vegetables, skipping rope and dumbbells on a wooden table"></div>
<svg class="abs play" width="88" height="88" viewBox="0 0 88 88">
  <circle cx="44" cy="44" r="38" fill="none" stroke="#fff" stroke-width="5"/>
  <polygon points="35,27 63,44 35,61" fill="#fff"/>
</svg>
<div class="abs heading about-title">ABOUT <em>VERDANT CORE</em></div>
<p class="abs about-text">Sed ut perspiciatis unde omnis iste natus error sit voluptatem accusantium doloremque laudantium, totam rem aperiam, eaque ipsa quae ab illo inventore veritatis et quasi architecto beatae vitae dicta sunt explicabo.</p>
<div class="abs btn-outline-white about-btn">READ MORE</div>

<!-- Coaching -->
<div class="abs coach-bg"></div>
<svg class="abs" style="left:0;top:1040px" width="1200" height="140" viewBox="0 0 1200 140">
  <polygon points="0,73 0,140 1200,140 1200,0" fill="var(--green)"/>
  <polygon points="620,98 1200,20 1200,110" fill="var(--sky)"/>
  <polygon points="880,82 1200,40 1200,60" fill="#6cc8ef"/>
</svg>
<div class="abs heading coach-title">COACHING</div>
<p class="abs coach-text">Sed ut perspiciatis unde omnis iste natus error sit voluptatem accusantium doloremque laudantium, totam rem aperiam, eaque ipsa quae ab illo inventore veritatis et quasi architecto beatae vitae dicta sunt explicabo. Nemo enim ipsam voluptatem quia voluptas sit aspernatur aut odit aut fugit,</p>
<div class="abs btn-outline-white coach-btn">READ MORE</div>
<div class="abs coach-photo" role="img" aria-label="Two personal trainers, one holding dumbbells and one holding a clipboard"></div>

<!-- Services -->
<div class="abs services-bg" role="img" aria-label="Dark background photo of fresh produce, grains and dumbbells"></div>
<svg class="abs" style="left:0;top:1630px" width="1200" height="60" viewBox="0 0 1200 60">
  <polygon points="0,0 0,60 400,60" fill="var(--lime)"/>
  <polygon points="0,0 400,60 1200,60 1200,50 0,0" fill="var(--blue)" opacity="0"/>
</svg>
<div class="abs heading services-title">SERVICES</div>
<div class="abs service-img s1" role="img" aria-label="Raw steak with fresh vegetables"></div>
<div class="abs service-img s2" role="img" aria-label="Athlete training with dumbbells"></div>
<div class="abs service-img s3" role="img" aria-label="Person working on a laptop with a phone"></div>
<div class="abs service-label" style="left:97px;top:2006px">NUTRITION<br>SERVICES</div>
<div class="abs service-label" style="left:450px;top:2006px">FITNESS<br>SERVICES</div>
<div class="abs service-label" style="left:801px;top:2006px">MOBILE AND ONLINE<br>SERVICES</div>

<!-- Testimonial -->
<div class="abs testi-bg"></div>
<svg class="abs" style="left:0;top:2078px" width="1200" height="120" viewBox="0 0 1200 120">
  <polygon points="0,120 1200,0 1200,120" fill="var(--blue)"/>
  <polygon points="0,120 1200,0 1200,30 700,120" fill="var(--green)"/>
  <polygon points="840,22 1200,0 1200,52" fill="var(--lime)"/>
</svg>
<svg class="abs" style="left:0;top:2560px" width="1200" height="60" viewBox="0 0 1200 60">
  <polygon points="0,30 350,42 0,60" fill="#163e66"/>
  <polygon points="0,40 350,42 0,50" fill="var(--lime)"/>
  <polygon points="0,60 350,42 1200,20 1200,60" fill="#26221e"/>
</svg>
<svg class="abs avatar" width="120" height="132" viewBox="0 0 120 132" role="img" aria-label="Client portrait">
  <polygon points="60,2 116,34 116,98 60,130 4,98 4,34" fill="#fff"/>
  <polygon points="60,8 110,37 110,95 60,124 10,95 10,37" fill="#c9a58c"/>
</svg>
<div class="abs t-name">Mara Ellison</div>
<div class="abs t-place">Portland, OR</div>
<p class="abs t-quote">Aorbi porta libero id ullamcorper nonummy nibh ligula pulvinar metus eget consectetuer augue nisi quis lacus Ut ac mi quis lacus</p>
<svg class="abs" style="left:90px;top:2394px" width="24" height="46" viewBox="0 0 24 46"><polyline points="22,2 3,23 22,44" fill="none" stroke="#fff" stroke-width="3"/></svg>
<svg class="abs" style="left:1082px;top:2394px" width="24" height="46" viewBox="0 0 24 46"><polyline points="2,2 21,23 2,44" fill="none" stroke="#fff" stroke-width="3"/></svg>
<div class="abs dots-line"></div>
<div class="abs dots"><span class="on"></span><span></span><span></span><span></span><span></span></div>

<!-- Booking -->
<div class="abs book-bg" role="img" aria-label="Dark background photo of crackers, nuts, water bottle and dumbbells"></div>
<div class="abs heading book-title">BOOK NOW</div>
<form class="abs form">
  <div class="field">NAME</div>
  <div class="field">DATE
    <svg width="12" height="12" viewBox="0 0 12 12"><rect x="1" y="2" width="10" height="9" fill="none" stroke="#fff"/><line x1="1" y1="5" x2="11" y2="5" stroke="#fff"/><line x1="4" y1="0" x2="4" y2="3" stroke="#fff"/><line x1="8" y1="0" x2="8" y2="3" stroke="#fff"/></svg>
  </div>
  <div class="field">TIME
    <svg width="12" height="12" viewBox="0 0 12 12"><circle cx="6" cy="6" r="5" fill="none" stroke="#fff"/><polyline points="6,3 6,6 8,7" fill="none" stroke="#fff"/></svg>
  </div>
  <div class="field msg">MESSAGE</div>
  <div class="submit">SUBMIT</div>
</form>
<div class="abs contact">
  <h3>CONTACT US</h3>
  <div class="c-label">ADDRESS</div>
  <div class="c-value">42 - 44 HARBOUR LANE, SYDNEY 2000</div>
  <div class="c-label">PHONE NUMBER</div>
  <div class="c-value">(555) 013 2240</div>
  <div class="c-label">EMAIL US</div>
  <div class="c-value">HELLO@VERDANTCORE.COM</div>
  <div class="c-label">FOLLOW US</div>
  <div class="social"><span></span><span></span><span></span><span></span></div>
</div>

<!-- Footer -->
<footer class="abs footer">© 2019 Verdant Core Nutritional Therapy. &nbsp;All right reserved</footer>

</body>
</html>
```